Grand Opening of Rosie's Tap, a craft beer bar in mountains of Payson AZ. Rosie is our black lab.

We need a card designed to advertise the grand opening of Rosie's Tap. It is a craft beer bar (we do not make our own beer but will highlight local beer) located next to Kestrel Lanes (which has also been rebranded). We will be serving craft beer and spirited drinks, along with a great burger (Rosie's Burger) and other bar food. The interior is a little industrial (corregated metal bar front) with a warm feel. We are trying to appeal to a more upscale crowd without being snobby. We would like it to be family friendly during the day.
Updates

Project Deadline Extended
Reason: I'm extending the deadline by 1 day so I have time to review updates. Thank you all for submissions!

```html
<!DOCTYPE html>
<html lang="en">
<head>
<meta charset="utf-8">
<title>Rosie's Tap – Grand Opening</title>
<link rel="stylesheet" href="https://fonts.googleapis.com/css2?family=Alegreya+SC:wght@500;700&family=Noticia+Text:wght@400&display=swap">
<style>
  :root {
    --metal-light: #b9bcbf;
    --metal-dark: #6f7377;
    --wood-light: #7a5238;
    --wood-dark: #3e2618;
    --gold-light: #f7e29a;
    --gold: #d4a63a;
    --gold-dark: #8a6418;
    --plate: #2f3033;
    --plate-light: #55575b;
    --red: #a3141a;
    --red-dark: #5e0a0e;
    --wheat-light: #f4ecd6;
    --wheat: #e0a33a;
    --white: #ffffff;
  }
  html, body { margin: 0; padding: 0; overflow: hidden; }
  body { width: 1200px; height: 931px; background: var(--metal-dark); }
  .card { position: relative; width: 1200px; height: 931px; overflow: hidden; }
  .shapes { position: absolute; inset: 0; }
  .text { position: absolute; left: 0; width: 1200px; text-align: center; color: var(--white); margin: 0; }
  .sc { font-family: "Alegreya SC", Georgia, serif; font-weight: 700; }
  .headline-plate { top: 104px; font-size: 76px; letter-spacing: 1px; font-weight: 500; transform: scaleX(0.9); }
  .bar-name { top: 222px; font-family: "Noticia Text", Georgia, serif; font-size: 170px; line-height: 1; text-shadow: 0 3px 6px rgba(0,0,0,.35); }
  .date { top: 432px; left: 400px; width: 400px; transform: rotate(3deg); line-height: 1; }
  .date .day { font-size: 46px; display: block; }
  .date .time { font-size: 22px; display: block; margin-top: 2px; }
  .lineup { top: 560px; font-size: 30px; line-height: 37px; font-weight: 500; text-shadow: 0 2px 3px rgba(0,0,0,.5); }
  .specials { top: 733px; line-height: 1.15; }
  .specials .main { font-size: 30px; display: block; }
  .specials .sub { font-size: 24px; display: block; }
  .badge { position: absolute; width: 200px; text-align: center; color: var(--white); font-size: 27px; line-height: 1.05; font-weight: 500; }
  .badge-prizes { left: 65px; top: 685px; }
  .badge-burgers { left: 935px; top: 685px; }
</style>
</head>
<body>
<main class="card">
  <svg class="shapes" width="1200" height="931" viewBox="0 0 1200 931" aria-hidden="false">
    <defs>
      <linearGradient id="metal" x1="0" y1="0" x2="0" y2="1">
        <stop offset="0" stop-color="var(--metal-light)"/>
        <stop offset="1" stop-color="var(--metal-dark)"/>
      </linearGradient>
      <linearGradient id="wood" x1="0" y1="0" x2="1" y2="0">
        <stop offset="0" stop-color="var(--wood-dark)"/>
        <stop offset=".5" stop-color="var(--wood-light)"/>
        <stop offset="1" stop-color="var(--wood-dark)"/>
      </linearGradient>
      <linearGradient id="gold" x1="0" y1="0" x2="0" y2="1">
        <stop offset="0" stop-color="var(--gold-light)"/>
        <stop offset=".5" stop-color="var(--gold)"/>
        <stop offset="1" stop-color="var(--gold-dark)"/>
      </linearGradient>
      <linearGradient id="plate" x1="0" y1="0" x2="1" y2="0">
        <stop offset="0" stop-color="var(--plate)"/>
        <stop offset=".5" stop-color="var(--plate-light)"/>
        <stop offset="1" stop-color="var(--plate)"/>
      </linearGradient>
      <linearGradient id="red" x1="0" y1="0" x2="1" y2="0">
        <stop offset="0" stop-color="var(--red-dark)"/>
        <stop offset=".5" stop-color="var(--red)"/>
        <stop offset="1" stop-color="var(--red-dark)"/>
      </linearGradient>
      <linearGradient id="wheat" x1="0" y1="0" x2="1" y2="0">
        <stop offset="0" stop-color="var(--wheat)"/>
        <stop offset=".6" stop-color="var(--wheat-light)"/>
      </linearGradient>
      <polygon id="star" points="1,0 .821,.220 .866,.5 .601,.601 .5,.866 .220,.821 0,1 -.220,.821 -.5,.866 -.601,.601 -.866,.5 -.821,.220 -1,0 -.821,-.220 -.866,-.5 -.601,-.601 -.5,-.866 -.220,-.821 0,-1 .220,-.821 .5,-.866 .601,-.601 .866,-.5 .821,-.220"/>
    </defs>

    <rect class="metal-band" x="0" y="0" width="1200" height="200" fill="url(#metal)" role="img" aria-label="Corrugated metal band"/>
    <rect class="metal-band" x="0" y="730" width="1200" height="201" fill="url(#metal)" role="img" aria-label="Corrugated metal band"/>
    <rect class="wood-panel" x="0" y="195" width="1200" height="540" fill="url(#wood)" role="img" aria-label="Warm wooden plank wall"/>

    <rect class="wheat" x="75" y="385" width="125" height="300" rx="60" fill="url(#wheat)" role="img" aria-label="Golden wheat ear"/>
    <rect class="wheat" x="1000" y="385" width="125" height="300" rx="60" fill="url(#wheat)" transform="matrix(-1 0 0 1 2125 0)" role="img" aria-label="Golden wheat ear"/>

    <g class="headline-plate-shape">
      <rect x="290" y="78" width="625" height="150" rx="75" fill="url(#gold)"/>
      <rect x="302" y="90" width="601" height="126" rx="63" fill="url(#plate)"/>
      <g fill="var(--gold-light)" stroke="var(--gold-dark)" stroke-width="1">
        <circle cx="350" cy="90" r="5"/><circle cx="597" cy="86" r="5"/><circle cx="853" cy="90" r="5"/>
        <circle cx="350" cy="216" r="5"/><circle cx="597" cy="220" r="5"/><circle cx="853" cy="216" r="5"/>
        <circle cx="302" cy="153" r="5"/><circle cx="903" cy="153" r="5"/>
      </g>
    </g>

    <g class="date-ribbon" transform="rotate(3 600 470)">
      <polygon points="330,455 420,445 420,540 350,560 375,505" fill="url(#gold)"/>
      <polygon points="340,462 420,452 420,532 362,550 385,505" fill="var(--plate)"/>
      <polygon points="870,455 780,445 780,540 850,560 825,505" fill="url(#gold)"/>
      <polygon points="860,462 780,452 780,532 838,550 815,505" fill="var(--plate)"/>
      <rect x="405" y="412" width="390" height="120" fill="url(#gold)"/>
      <rect x="415" y="422" width="370" height="100" fill="url(#plate)"/>
    </g>

    <g class="specials-pill">
      <rect x="355" y="718" width="488" height="120" rx="60" fill="url(#gold)"/>
      <rect x="365" y="728" width="468" height="100" rx="50" fill="url(#red)"/>
    </g>

    <g class="starburst" transform="translate(165 712)">
      <use href="#star" transform="scale(108)" fill="url(#gold)"/>
      <use href="#star" transform="scale(94)" fill="url(#plate)"/>
    </g>
    <g class="starburst" transform="translate(1035 712)">
      <use href="#star" transform="scale(108)" fill="url(#gold)"/>
      <use href="#star" transform="scale(94)" fill="url(#plate)"/>
    </g>
  </svg>

  <p class="text sc headline-plate">Grand Opening</p>
  <h1 class="text bar-name">Rosie's Tap</h1>
  <p class="text sc date"><span class="day">September 19th</span><span class="time">at 4pm.</span></p>
  <p class="text sc lineup">Live entertainment by:<br>BandX on Friday night<br>Danny Ferrante &amp; the Hot Macchiatos<br>on Saturday night and Sunday afternoon.</p>
  <p class="text sc specials"><span class="main">$3 Craft beers</span><span class="sub">and Spirited Drinks Specials</span><span class="sub">all weekend</span></p>
  <p class="badge sc badge-prizes">Door<br>Prizes</p>
  <p class="badge sc badge-burgers">Great<br>Burgers</p>
</main>
</body>
</html>
```